Travel Agency Website - Simple General

Need a 7 page simple design that is pretty repetitive. Need to be able to load quickly that is SEO optimized. Trying to give ideas on what they can do, be personal as we are local, but at the same time come across as professional and get information easily with little burden.

- Landing Page
- Brambleton Vacations Page
- Family Trips
- Road Trips from Texas
- Other Destinations
- About Us Page
- Contact Us Page

Target Market(s)

Families

Coding

Coded - Design and coding required

Number of Pages Required

5+ page

Colors

Designer to choose colors to be used in the design.

Requirements
Must have
• Like it to flow easily with our logo. Use that for colors, etc.

```html
<!DOCTYPE html>
<html lang="en">
<head>
<meta charset="utf-8">
<title>Hum Along Holidays – Travel Planning</title>
<link href="https://fonts.googleapis.com/css2?family=Inter:wght@400;500;600;700;800&display=swap" rel="stylesheet">
<style>
:root{
  --teal:#1f5662;
  --teal-dark:#173f4a;
  --gold:#b98c45;
  --gold-light:#d9b678;
  --ink:#222b30;
  --muted:#55626a;
  --sky:#e7f7fb;
  --white:#ffffff;
  --line:#c9cfd2;
}
*{margin:0;padding:0;box-sizing:border-box}
html,body{width:1200px;height:4684px;overflow:hidden}
body{position:relative;font-family:"Inter",Arial,sans-serif;color:var(--ink);background:var(--white)}
.abs{position:absolute}
a{color:inherit;text-decoration:none}

/* top bar */
.topbar{left:0;top:0;width:1200px;height:36px;background:var(--teal);color:#fff;font-size:15px;display:flex;align-items:center;justify-content:flex-end;padding-right:82px;gap:10px}
.topbar svg{width:16px;height:16px}

/* hero */
.hero{left:0;top:36px;width:1200px;height:655px;background:radial-gradient(ellipse at 30% 45%,#3b5668 0%,#24394a 55%,#1b2c3a 100%)}
.nav{left:65px;top:51px;width:1068px;height:98px;background:#fff;border-radius:49px;box-shadow:0 4px 18px rgba(0,0,0,.15)}
.brand{left:38px;top:36px;font-size:19px;font-weight:700;color:var(--teal);display:flex;align-items:center;gap:8px}
.brand i{display:block;width:14px;height:14px;border-radius:50%;background:var(--gold)}
.nav-links{left:428px;top:38px;font-size:17px;color:var(--teal)}
.nav-links a{position:absolute;white-space:nowrap}
.btn{display:inline-flex;align-items:center;justify-content:center;background:var(--gold);color:#fff;font-weight:600;border-radius:3px;white-space:nowrap}
.nav .btn{left:882px;top:29px;width:133px;height:40px;font-size:16px}
.hero-title{left:125px;top:296px;font-size:50px;line-height:57px;font-weight:700;color:#fff}
.hero-text{left:125px;top:415px;width:325px;font-size:15px;line-height:20px;color:#f2f2f2}
.btn-ghost{top:509px;height:40px;font-size:15px;display:inline-flex;align-items:center;justify-content:center;border:2px solid #fff;color:#fff;font-weight:600;border-radius:3px}
.hero-photo{left:523px;top:167px;width:526px;height:497px;border-radius:120px 120px 120px 120px/90px;background:radial-gradient(circle at 50% 60%,#d8d0c0 0%,#a79373 40%,#5d6a5a 75%,#3d4a40 100%);border:3px solid var(--gold)}

/* headings */
.section-title{left:0;width:1200px;text-align:center;font-size:47px;font-weight:700;color:var(--teal)}
.section-title em{font-style:normal;color:var(--gold)}
.section-sub{left:0;width:1200px;text-align:center;font-size:16px;line-height:21px;color:var(--ink)}

/* specialties */
.dash{border:1.5px dashed var(--line);border-radius:12px}
.spec-photo{width:291px;height:251px;border-radius:70px/55px;box-shadow:0 6px 14px rgba(0,0,0,.12)}
.spec-card{width:384px;height:256px;background:#fff;border:2px solid #ececec;border-radius:16px;box-shadow:0 4px 14px rgba(0,0,0,.08);padding:38px 36px 0}
.tag{display:inline-block;border:1.5px solid var(--teal);color:var(--teal);font-size:14px;font-weight:500;padding:6px 12px;border-radius:2px}
.spec-card h3{margin-top:14px;font-size:20px;font-weight:600;color:var(--gold)}
.spec-card p{margin-top:12px;font-size:14.5px;line-height:20px;color:var(--ink);width:300px}
.spec-card .btn{margin-top:12px;height:35px;padding:0 12px;font-size:14.5px}

/* why name */
.band{left:0;width:1200px;background:var(--sky)}
.name-title{left:125px;top:2600px;font-size:48px;line-height:57px;font-weight:700;color:var(--teal)}
.name-title em{font-style:normal;color:var(--gold)}
.name-text{left:125px;top:2778px;width:390px;font-size:14.5px;line-height:20px;color:var(--ink)}
.name-frame{left:560px;top:2600px;width:500px;height:345px;border:2px solid var(--gold);border-radius:22px;transform:rotate(5deg)}
.name-photo{left:578px;top:2620px;width:467px;height:316px;border-radius:22px;background:radial-gradient(circle at 30% 40%,#f0b15a 0%,#b66a2a 30%,#4b3320 65%,#221a14 100%)}

/* features */
.feature{top:3320px;width:307px;height:261px;background:#fff;border:2px solid #ececec;border-radius:12px;box-shadow:0 4px 12px rgba(0,0,0,.08);text-align:center}
.feature .icon{width:90px;height:90px;margin:26px auto 0;border-radius:14px;background:linear-gradient(135deg,#f3e6cf,#e2c693)}
.feature h3{margin-top:22px;font-size:20px;font-weight:600;color:var(--teal)}
.feature p{margin:6px auto 0;width:265px;font-size:14.5px;line-height:18px}

/* testimonials */
.quote{top:3978px;width:307px;height:304px;background:#fff;border:2px solid #ececec;border-radius:12px;box-shadow:0 4px 12px rgba(0,0,0,.08);padding:26px 26px 0}
.stars{display:flex;gap:8px}
.stars svg{width:21px;height:21px;fill:#f2b01e}
.quote p{margin-top:18px;font-size:12.5px;line-height:16px}
.who{position:absolute;left:26px;top:214px;display:flex;align-items:center;gap:10px}
.avatar{width:49px;height:49px;border-radius:50%;background:var(--gold);color:#fff;font-weight:600;font-size:18px;display:flex;align-items:center;justify-content:center}
.who b{display:block;font-size:19px;font-weight:600;color:var(--gold)}
.who span{font-size:12.5px}

/* footer */
.footer{left:0;top:4400px;width:1200px;height:284px;background:var(--teal);color:#fff}
.foot-brand{left:127px;top:63px;width:164px;height:137px;border-radius:50%;background:#fff;display:flex;align-items:center;justify-content:center;text-align:center;color:var(--teal);font-weight:700;font-size:19px;line-height:22px}
.foot-col{top:82px}
.foot-col h4{font-size:20px;font-weight:600;color:var(--gold);margin-bottom:10px}
.foot-col li{list-style:none;font-size:13px;line-height:29px;display:flex;align-items:center;gap:8px}
.foot-col li::before{content:"";width:5px;height:5px;border-radius:50%;background:var(--gold)}
.contact-row{display:flex;align-items:center;gap:12px;font-size:15px;line-height:32px}
.contact-row svg{width:17px;height:17px}
.socials{display:flex;gap:14px;margin-top:12px}
.socials span{width:36px;height:36px;border-radius:50%;background:#fff;display:block}
.copyright{left:0;top:4646px;width:1200px;text-align:center;font-size:12.5px;color:#e6eef0}
.rule{left:0;width:1200px;height:1px;background:rgba(255,255,255,.2)}
</style>
</head>
<body>

<div class="abs topbar">For More Information Contact Us
  <svg viewBox="0 0 24 24" fill="#d9b678"><path d="M6.6 10.8a15.1 15.1 0 0 0 6.6 6.6l2.2-2.2a1 1 0 0 1 1-.25 11.4 11.4 0 0 0 3.6.57 1 1 0 0 1 1 1V20a1 1 0 0 1-1 1A17 17 0 0 1 3 4a1 1 0 0 1 1-1h3.5a1 1 0 0 1 1 1c0 1.25.2 2.45.57 3.57a1 1 0 0 1-.25 1z"/></svg>
  555.014.2290</div>

<header class="abs hero">
  <div role="img" aria-label="Faint world map pattern behind the hero" class="abs" style="inset:0"></div>
</header>

<nav class="abs nav">
  <div class="abs brand"><i></i>Hum Along Holidays</div>
  <div class="abs nav-links">
    <a style="left:0">Home</a>
    <a style="left:78px">Destinations</a>
    <a style="left:209px">About Us</a>
    <a style="left:312px">Contact Us</a>
  </div>
  <a class="abs btn">Plan Your Trip</a>
</nav>

<h1 class="abs hero-title">Hum Along<br>Holidays</h1>
<p class="abs hero-text">Your dream vacation starts here. From the magic of Brambleton to scenic Texas road trips, we craft personalized travel experiences that you'll cherish forever.</p>
<a class="abs btn" style="left:125px;top:509px;width:172px;height:40px;font-size:15px">Explore Destinations</a>
<a class="abs btn-ghost" style="left:311px;width:134px">Our Philosophy</a>
<div class="abs hero-photo" role="img" aria-label="Photo of a white motorhome parked outdoors at sunset"></div>

<!-- specialties -->
<h2 class="abs section-title" style="top:845px">Where is Your Heart <em>Whispering</em> to Go?</h2>
<p class="abs section-sub" style="top:912px">Select one of our four core specialties below to dive into curated itineraries, custom services, and premium options<br>designed specifically for your travel style.</p>

<div class="abs dash" style="left:276px;top:1018px;width:457px;height:295px"></div>
<div class="abs spec-photo" role="img" aria-label="Photo of a traveler walking toward an old stone fortress" style="left:127px;top:1045px;background:linear-gradient(160deg,#9fb6c8,#c79a5c 55%,#7d5a36)"></div>
<div class="abs spec-card" style="left:529px;top:1040px">
  <span class="tag">LAND &amp; SEA</span>
  <h3>Brambleton Vacations</h3>
  <p>Experience the magic of Brambleton at the parks or aboard a Brambleton Cruise Line adventure.</p>
  <a class="btn">Discover Magic</a>
</div>

<div class="abs dash" style="left:442px;top:1349px;width:454px;height:296px"></div>
<div class="abs spec-photo" role="img" aria-label="Photo of a family walking hand in hand on a beach" style="left:295px;top:1373px;background:linear-gradient(180deg,#e9e4dc,#cbb9a1 60%,#a58c6c)"></div>
<div class="abs spec-card" style="left:693px;top:1371px">
  <span class="tag">Memories First</span>
  <h3>Family Trips</h3>
  <p>Flawless travel plans for multi-generational gatherings, active kids, and stress-free packing.</p>
  <a class="btn">Explore Journeys</a>
</div>

<div class="abs dash" style="left:276px;top:1676px;width:457px;height:300px"></div>
<div class="abs spec-photo" role="img" aria-label="Photo of a camper van parked by the sea among tall grass" style="left:127px;top:1703px;background:linear-gradient(180deg,#c7dde8,#6f9bb2 45%,#c9b07a 70%,#8e7a4c)"></div>
<div class="abs spec-card" style="left:529px;top:1700px">
  <span class="tag">VAN RENTAL PARTNER</span>
  <h3>Texas Road Trips</h3>
  <p>Partnered with Piney Trail Van Rentals to deliver premium transportation and routes from deep woods to sandy shores.</p>
  <a class="btn">Hit the Road</a>
</div>

<div class="abs dash" style="left:442px;top:2007px;width:454px;height:300px"></div>
<div class="abs spec-photo" role="img" aria-label="Photo of a tropical resort with a volcano-shaped rock and palm trees" style="left:295px;top:2033px;background:linear-gradient(180deg,#dbe7ee,#a47b5c 45%,#4f7a3f 75%,#2f5a3a)"></div>
<div class="abs spec-card" style="left:693px;top:2031px">
  <span class="tag">GO GLOBAL</span>
  <h3>Other Destinations</h3>
  <p>Custom global travel packages including European escapes, tropical resorts, and customized boutique tours.</p>
  <a class="btn">Wander Globally</a>
</div>

<!-- why the name -->
<section class="abs band" style="top:2485px;height:551px"></section>
<h2 class="abs name-title">Why the Name<br><em>"Hum Along<br>Holidays"</em>?</h2>
<p class="abs name-text">Think of the classic, cheerful tune—it's all about finding lighthearted joy, peace, and music in everything you do. Travel planning should never feel like a tedious chore, yet modern bookings have become incredibly complicated with park reservations, skip-the-line strategies, rental coordination, and hotel availability puzzles.</p>
<a class="abs btn" style="left:125px;top:2925px;width:108px;height:37px;font-size:14.5px">Read More</a>
<div class="abs name-frame"></div>
<div class="abs name-photo" role="img" aria-label="Photo of a camper with glowing lanterns in a forest at dusk"></div>

<!-- why with us -->
<h2 class="abs section-title" style="top:3192px">Why <em>Hum</em> With Us?</h2>
<p class="abs section-sub" style="top:3260px">We take care of every detail so you can focus on making memories.</p>

<div class="abs feature" style="left:124px">
  <div class="icon" role="img" aria-label="Icon of a planning document with a compass"></div>
  <h3>Personalized Planning</h3>
  <p>Every trip is custom-tailored to your preferences, budget, and dreams. No two itineraries are alike.</p>
</div>
<div class="abs feature" style="left:447px">
  <div class="icon" role="img" aria-label="Icon of a handshake beneath a star"></div>
  <h3>Trusted Partnerships</h3>
  <p>We work with top vendors like Piney Trail Van Rentals to ensure seamless travel experiences.</p>
</div>
<div class="abs feature" style="left:769px">
  <div class="icon" role="img" aria-label="Icon of photos and a camera"></div>
  <h3>Magical Moments</h3>
  <p>From Brambleton fireworks to hidden Texas gems, we know how to find the magic in every journey.</p>
</div>

<!-- testimonials -->
<section class="abs band" style="top:3760px;height:640px"></section>
<h2 class="abs section-title" style="top:3848px">What Happy <em>Wanderers</em> Say</h2>

<div class="abs quote" style="left:124px">
  <div class="stars"><svg viewBox="0 0 24 24"><path d="M12 2l3 7 7.5.6-5.7 4.9 1.8 7.4L12 18l-6.6 3.9 1.8-7.4L1.5 9.6 9 9z"/></svg><svg viewBox="0 0 24 24"><path d="M12 2l3 7 7.5.6-5.7 4.9 1.8 7.4L12 18l-6.6 3.9 1.8-7.4L1.5 9.6 9 9z"/></svg><svg viewBox="0 0 24 24"><path d="M12 2l3 7 7.5.6-5.7 4.9 1.8 7.4L12 18l-6.6 3.9 1.8-7.4L1.5 9.6 9 9z"/></svg><svg viewBox="0 0 24 24"><path d="M12 2l3 7 7.5.6-5.7 4.9 1.8 7.4L12 18l-6.6 3.9 1.8-7.4L1.5 9.6 9 9z"/></svg><svg viewBox="0 0 24 24"><path d="M12 2l3 7 7.5.6-5.7 4.9 1.8 7.4L12 18l-6.6 3.9 1.8-7.4L1.5 9.6 9 9z"/></svg></div>
  <p>"Booking our Brambleton World and Brambleton Cruise vacation with Hum Along Holidays was the best decision ever. We didn't have to stay up at 5:00 AM to make dining reservations—they handled everything! Complete bliss."</p>
  <div class="who"><div class="avatar">MF</div><div><b>The Miller Family</b><span>Brambleton Cruise &amp; Land Traveler</span></div></div>
</div>
<div class="abs quote" style="left:447px">
  <div class="stars"><svg viewBox="0 0 24 24"><path d="M12 2l3 7 7.5.6-5.7 4.9 1.8 7.4L12 18l-6.6 3.9 1.8-7.4L1.5 9.6 9 9z"/></svg><svg viewBox="0 0 24 24"><path d="M12 2l3 7 7.5.6-5.7 4.9 1.8 7.4L12 18l-6.6 3.9 1.8-7.4L1.5 9.6 9 9z"/></svg><svg viewBox="0 0 24 24"><path d="M12 2l3 7 7.5.6-5.7 4.9 1.8 7.4L12 18l-6.6 3.9 1.8-7.4L1.5 9.6 9 9z"/></svg><svg viewBox="0 0 24 24"><path d="M12 2l3 7 7.5.6-5.7 4.9 1.8 7.4L12 18l-6.6 3.9 1.8-7.4L1.5 9.6 9 9z"/></svg><svg viewBox="0 0 24 24"><path d="M12 2l3 7 7.5.6-5.7 4.9 1.8 7.4L12 18l-6.6 3.9 1.8-7.4L1.5 9.6 9 9z"/></svg></div>
  <p>"Our road trip with Piney Trail Van Rentals was unbelievable. The luxury touring van with reclining captain chairs kept the kids comfortable and quiet. Hum Along Holidays co-curated our Hill Country stops flawlessly!"</p>
  <div class="who"><div class="avatar">JH</div><div><b>James H.</b><span>Texas Hill Country Wanderer</span></div></div>
</div>
<div class="abs quote" style="left:769px">
  <div class="stars"><svg viewBox="0 0 24 24"><path d="M12 2l3 7 7.5.6-5.7 4.9 1.8 7.4L12 18l-6.6 3.9 1.8-7.4L1.5 9.6 9 9z"/></svg><svg viewBox="0 0 24 24"><path d="M12 2l3 7 7.5.6-5.7 4.9 1.8 7.4L12 18l-6.6 3.9 1.8-7.4L1.5 9.6 9 9z"/></svg><svg viewBox="0 0 24 24"><path d="M12 2l3 7 7.5.6-5.7 4.9 1.8 7.4L12 18l-6.6 3.9 1.8-7.4L1.5 9.6 9 9z"/></svg><svg viewBox="0 0 24 24"><path d="M12 2l3 7 7.5.6-5.7 4.9 1.8 7.4L12 18l-6.6 3.9 1.8-7.4L1.5 9.6 9 9z"/></svg><svg viewBox="0 0 24 24"><path d="M12 2l3 7 7.5.6-5.7 4.9 1.8 7.4L12 18l-6.6 3.9 1.8-7.4L1.5 9.6 9 9z"/></svg></div>
  <p>"We spent two weeks on a tailor-made European vacation. Every transfer was on time, the boutique hotels in Italy were stunning, and our English-speaking guides were so knowledgeable. They really made it a joy!"</p>
  <div class="who"><div class="avatar">SR</div><div><b>Sarah &amp; Robert</b><span>European Custom Itinerary</span></div></div>
</div>

<!-- footer -->
<footer class="abs footer">
  <div class="abs foot-brand">Hum Along<br>Holidays</div>
  <div class="abs foot-col" style="left:351px">
    <h4>Destinations</h4>
    <ul><li>Brambleton Vacations</li><li>Family Trips</li><li>Texas Road Trips</li><li>Other Destinations</li></ul>
  </div>
  <div class="abs foot-col" style="left:555px">
    <h4>Quick Links</h4>
    <ul><li>Home</li><li>Destination</li><li>About Us</li><li>Contact Us</li></ul>
  </div>
  <div class="abs foot-col" style="left:755px">
    <h4>Contact &amp; Partners</h4>
    <div class="contact-row"><svg viewBox="0 0 24 24" fill="#d9b678"><path d="M6.6 10.8a15.1 15.1 0 0 0 6.6 6.6l2.2-2.2a1 1 0 0 1 1-.25 11.4 11.4 0 0 0 3.6.57 1 1 0 0 1 1 1V20a1 1 0 0 1-1 1A17 17 0 0 1 3 4a1 1 0 0 1 1-1h3.5a1 1 0 0 1 1 1c0 1.25.2 2.45.57 3.57a1 1 0 0 1-.25 1z"/></svg><span style="font-size:13px">555.014.2290</span></div>
    <div class="contact-row"><svg viewBox="0 0 24 24" fill="#d9b678"><path d="M2 5h20v14H2z"/><path d="M2 5l10 8 10-8" stroke="#1f5662" stroke-width="2" fill="none"/></svg>HumAlongHolidays@mailbox.example</div>
    <div class="socials"><span></span><span></span></div>
  </div>
  <div class="abs rule" style="top:234px"></div>
</footer>
<p class="abs copyright">© 2026 Hum Along Holidays Travel. All Rights Reserved. Co-branded &amp; developed in partnership with Piney Trail Van Rentals.</p>

</body>
</html>
```